Personal Injury Law Firm Marketing Postcards

Looking for 4 different high quality graphic postcards (print on both sides of 4"x6" postcard to market a Personal Injury Lawyer (Walter Gimsby). These will be placed on cars and in stores on stands. My photo and/or stock images.... We are targeting People who have been injured in automobile accidents, motorcycle accidents, slip and fall (wet/greasy floors indoors in supermarkets, restaurants, etc., snow and ice outdoors on sidewalks) trip and fall cases on dangerous staircases. indoor/outdoor, dog bite injuries. ( I like the use of stock images of these type of injury causing accidents. You can use following language "Serving People Injured in NY & NJ" . Millions of Dollars Recovered, Free Consultation and No Fee Unless We Recover Money! Phone number to be displayed (555) 418-3062 "call or text" Available 24 hours a day 7 days per week. May also want to mention that we can take over your case from another lawyer if you are not satisfied with your current attorney. There should be a small space in corner which has a space for my marketing person to handwrite in their reference code.

Target Market(s)

18-75 years old - densely populated major city

Industry/Entity Type

Legal

Font styles to use
Other font styles liked:
• Please use logo style that I uploaded.. Please do not just cut parts of my website out and use them. Do not use LOGO from my website

Colors
0054AA
0677BA
7BADD7
CADEEF
E8F1F8
00AB8E
00BBA5
67D7C9
C6EFE9
E9F9F6

Requirements
Must have
• Professional Appearance

```html
<!DOCTYPE html>
<html lang="en">
<head>
<meta charset="utf-8">
<title>Walter Gimsby Law Office – Postcard</title>
<link href="https://fonts.googleapis.com/css2?family=Poppins:wght@400;500;600;700&family=Libre+Baskerville:wght@700&display=swap" rel="stylesheet">
<style>
  :root{
    --stage:#a4a4a4;
    --navy:#0c2a55;
    --navy-deep:#0a2247;
    --blue:#0a6cc0;
    --gold:#c9a24a;
    --gold-light:#e2c676;
    --white:#ffffff;
    --ink:#2c3440;
    --stamp:#a7a9ac;
  }
  *{margin:0;padding:0;box-sizing:border-box}
  html,body{width:1200px;height:1117px;overflow:hidden}
  body{background:var(--stage);font-family:"Poppins",sans-serif;position:relative}
  .card{position:absolute;left:235px;width:730px;height:486px;overflow:hidden}
  .card--front{top:57px;background:var(--navy)}
  .card--back{top:569px;background:linear-gradient(160deg,#ffffff 55%,#eeeeee)}
  .layer{position:absolute;left:0;top:0}
  .brand{position:absolute;color:var(--gold);font-weight:600;text-transform:uppercase;line-height:1.02;letter-spacing:-.5px}
  .brand--front{left:24px;top:152px;font-size:27px}
  .headline{position:absolute;left:257px;top:282px;font-family:"Libre Baskerville",serif;color:var(--white);font-size:24px;line-height:1.12;text-transform:uppercase}
  .headline__sub{display:block;color:var(--gold);font-size:17px;line-height:1.15;margin-top:2px}
  .tagline{position:absolute;left:43px;top:392px;color:var(--white);font-size:13.4px;font-weight:400}
  .contact-bar{position:absolute;left:0;top:442px;width:730px;height:24px;display:flex;align-items:center;color:var(--white);font-weight:600;font-size:16.5px}
  .contact-bar__item{position:absolute;display:flex;align-items:center;gap:8px;top:0;height:24px}
  .contact-bar__divider{position:absolute;top:0;width:2px;height:26px;background:var(--white)}
  .icon-dot{width:17px;height:17px;border-radius:50%;background:var(--gold);display:flex;align-items:center;justify-content:center;flex:none}
  .services-title{position:absolute;left:109px;top:9px;width:147px;text-align:center;color:var(--white);font-weight:600;font-size:21px}
  .service{position:absolute;display:flex;align-items:center;gap:8px}
  .service__badge{width:34px;height:34px;border-radius:50%;border:2.5px solid var(--blue);display:flex;align-items:center;justify-content:center;background:#fff;flex:none}
  .service__art{width:20px;height:20px;border-radius:50%;background:linear-gradient(#b9bec6,#8f96a0)}
  .service__label{font-size:6.8px;line-height:1.35;color:var(--ink);text-transform:uppercase;font-weight:500}
  .switch-note{position:absolute;left:0;top:205px;width:347px;height:67px;background:var(--navy);color:var(--white);font-size:12.6px;line-height:1.1;text-align:center;padding-top:12px}
  .availability{position:absolute;left:27px;top:385px;color:var(--white);font-weight:600;font-size:8.4px;line-height:1.2}
  .phone-big{position:absolute;left:27px;top:406px;display:flex;align-items:center;gap:9px;color:var(--white);font-weight:700;font-size:21px}
  .contact-line{position:absolute;left:27px;display:flex;align-items:center;gap:10px;color:var(--white);font-size:13px}
  .brand--back{left:278px;top:420px;width:60px;text-align:center;font-size:7.2px;letter-spacing:-.2px;font-weight:600}
  .stamp-box{position:absolute;left:624px;top:23px;width:77px;height:77px;background:var(--stamp)}
</style>
</head>
<body>

<!-- FRONT -->
<section class="card card--front">
  <svg class="layer" width="730" height="486" viewBox="0 0 730 486">
    <defs>
      <linearGradient id="scene" x1="0" y1="0" x2="1" y2="1">
        <stop offset="0" stop-color="#4a4a4e"/>
        <stop offset=".45" stop-color="#8c8f98"/>
        <stop offset="1" stop-color="#b9a99a"/>
      </linearGradient>
      <linearGradient id="portrait" x1="0" y1="0" x2="0" y2="1">
        <stop offset="0" stop-color="#6b6a70"/>
        <stop offset=".5" stop-color="#3e4150"/>
        <stop offset="1" stop-color="#242a3a"/>
      </linearGradient>
      <linearGradient id="goldBand" x1="0" y1="0" x2="1" y2="1">
        <stop offset="0" stop-color="#b98f38"/>
        <stop offset=".5" stop-color="#ecd48b"/>
        <stop offset="1" stop-color="#b98f38"/>
      </linearGradient>
      <linearGradient id="panel" x1="0" y1="0" x2="1" y2="1">
        <stop offset="0" stop-color="#ffffff"/>
        <stop offset="1" stop-color="#ececec"/>
      </linearGradient>
    </defs>
    <rect x="217" y="0" width="513" height="244" fill="url(#scene)" role="img" aria-label="Photo of rescue workers at an overturned car after a crash"/>
    <rect x="525" y="0" width="205" height="423" fill="url(#portrait)" role="img" aria-label="Portrait photo of the attorney in a suit"/>
    <rect x="257" y="255" width="295" height="8" fill="url(#goldBand)"/>
    <polygon points="0,0 240,0 240,0 328,169 240,374 0,374" fill="var(--navy)"/>
    <polygon points="0,0 218,0 306,169 209,374 0,374" fill="url(#goldBand)"/>
    <polygon points="0,0 187,0 290,169 181,356 0,356" fill="url(#panel)"/>
    <polygon points="37,423 730,423 730,486 0,486" fill="var(--blue)"/>
  </svg>

  <div class="brand brand--front">Law Office of<br>Walter Gimsby</div>

  <h1 class="headline">Personal<br>Injury Lawyer
    <span class="headline__sub">Serves all of New Jersey<br>and New York.</span>
  </h1>

  <p class="tagline">Millions of Dollars Recovered, Free Consultation and No Fee Unless We Recover Money!</p>

  <div class="contact-bar">
    <div class="contact-bar__item" style="left:54px">
      <span class="icon-dot"><svg width="11" height="11" viewBox="0 0 12 12" fill="none" stroke="#0a6cc0" stroke-width="1.1"><circle cx="6" cy="6" r="5"/><ellipse cx="6" cy="6" rx="2.2" ry="5"/><line x1="1" y1="6" x2="11" y2="6"/></svg></span>
      www.wglegal.com
    </div>
    <span class="contact-bar__divider" style="left:256px"></span>
    <div class="contact-bar__item" style="left:271px">
      <span class="icon-dot"><svg width="10" height="8" viewBox="0 0 10 8" fill="none" stroke="#0a6cc0" stroke-width="1"><rect x=".5" y=".5" width="9" height="7"/><polyline points=".5,.5 5,4.5 9.5,.5"/></svg></span>
      wgimsby@wglegal.com
    </div>
    <span class="contact-bar__divider" style="left:513px"></span>
    <div class="contact-bar__item" style="left:527px">
      <span class="icon-dot"><svg width="10" height="10" viewBox="0 0 24 24" fill="#0a6cc0"><path d="M6.6 10.8a15.1 15.1 0 0 0 6.6 6.6l2.2-2.2a1 1 0 0 1 1-.25 11.4 11.4 0 0 0 3.6.57 1 1 0 0 1 1 1V20a1 1 0 0 1-1 1A17 17 0 0 1 3 4a1 1 0 0 1 1-1h3.5a1 1 0 0 1 1 1c0 1.25.2 2.45.57 3.57a1 1 0 0 1-.25 1z"/></svg></span>
      (555) 418-3062
    </div>
  </div>
</section>

<!-- BACK -->
<section class="card card--back">
  <svg class="layer" width="730" height="486" viewBox="0 0 730 486">
    <defs>
      <linearGradient id="goldTab" x1="0" y1="0" x2="1" y2="0">
        <stop offset="0" stop-color="#b98f38"/>
        <stop offset=".5" stop-color="#e2c676"/>
        <stop offset="1" stop-color="#b98f38"/>
      </linearGradient>
      <linearGradient id="street" x1="0" y1="0" x2="1" y2="0">
        <stop offset="0" stop-color="#7f848c"/>
        <stop offset=".6" stop-color="#a9adb3"/>
        <stop offset="1" stop-color="#55595f"/>
      </linearGradient>
    </defs>
    <rect x="0" y="0" width="347" height="205" fill="#fff"/>
    <rect x="0" y="0" width="347" height="8" fill="url(#goldTab)"/>
    <polygon points="109,8 256,8 238,40 127,40" fill="url(#goldTab)"/>
    <g fill="none" stroke="var(--gold)" stroke-width="1.6">
      <polyline points="62,26 18,26 18,70"/>
      <polyline points="303,26 347,26 347,70"/>
      <polyline points="18,146 18,191 62,191"/>
      <polyline points="347,146 347,191 303,191"/>
    </g>
    <rect x="0" y="272" width="347" height="106" fill="url(#street)" role="img" aria-label="Photo of a car speeding past a pedestrian at a crosswalk"/>
    <polygon points="0,325 24,378 220,378 284,486 0,486" fill="var(--blue)"/>
  </svg>

  <div class="services-title">Services</div>

  <div class="service" style="left:34px;top:50px"><span class="service__badge"><span class="service__art" role="img" aria-label="Dog icon"></span></span><span class="service__label">Dog bites /<br>attacks</span></div>
  <div class="service" style="left:131px;top:50px"><span class="service__badge"><span class="service__art" role="img" aria-label="Falling person icon"></span></span><span class="service__label">Trip and fall<br>accidents</span></div>
  <div class="service" style="left:228px;top:50px"><span class="service__badge"><span class="service__art" role="img" aria-label="Scales icon"></span></span><span class="service__label">Wrongful<br>death attorneys</span></div>

  <div class="service" style="left:34px;top:95px"><span class="service__badge"><span class="service__art" role="img" aria-label="Injured worker icon"></span></span><span class="service__label">Workplace<br>accidents</span></div>
  <div class="service" style="left:131px;top:95px"><span class="service__badge"><span class="service__art" role="img" aria-label="Truck icon"></span></span><span class="service__label">Truck<br>accidents</span></div>
  <div class="service" style="left:228px;top:95px"><span class="service__badge"><span class="service__art" role="img" aria-label="Slipping person icon"></span></span><span class="service__label">Slip and<br>fall accidents</span></div>

  <div class="service" style="left:34px;top:141px"><span class="service__badge"><span class="service__art" role="img" aria-label="Motorcycle icon"></span></span><span class="service__label">Motorcycle<br>accidents</span></div>
  <div class="service" style="left:131px;top:141px"><span class="service__badge"><span class="service__art" role="img" aria-label="Pedestrian icon"></span></span><span class="service__label">Pedestrian<br>accidents</span></div>
  <div class="service" style="left:228px;top:141px"><span class="service__badge"><span class="service__art" role="img" aria-label="Car icon"></span></span><span class="service__label">Car<br>accidents</span></div>

  <p class="switch-note">We can take over your case from another<br>lawyer if you are not satisfied with your<br>current attorney.</p>

  <p class="availability">call or text Available 24 hours a day<br>7 days per week.</p>

  <div class="phone-big">
    <span class="icon-dot" style="width:21px;height:21px"><svg width="12" height="12" viewBox="0 0 24 24" fill="#0a6cc0"><path d="M6.6 10.8a15.1 15.1 0 0 0 6.6 6.6l2.2-2.2a1 1 0 0 1 1-.25 11.4 11.4 0 0 0 3.6.57 1 1 0 0 1 1 1V20a1 1 0 0 1-1 1A17 17 0 0 1 3 4a1 1 0 0 1 1-1h3.5a1 1 0 0 1 1 1c0 1.25.2 2.45.57 3.57a1 1 0 0 1-.25 1z"/></svg></span>
    (555) 418-3062
  </div>
  <div class="contact-line" style="top:434px"><span class="icon-dot" style="width:12px;height:12px"></span>www.wglegal.com</div>
  <div class="contact-line" style="top:451px"><span class="icon-dot" style="width:12px;height:12px"></span>wgimsby@wglegal.com</div>

  <div class="brand brand--back">Law Office of<br>Walter Gimsby</div>

  <div class="stamp-box" aria-label="Stamp area"></div>
</section>

</body>
</html>
```